Flyer for Compassion training days

I need a A5-size, single-sided flyer design for my training days. They are weekends in a blend of Compassionate Communication and Buddhist teachings called Palomere Communication. The logo for Palomere that should be included.
The flyer needs room for 1) course title, 2) course dates, location & price, 3) course description, 4) booking info, 5) my picture & short bio, and 6) the palomere.co website (yes, it is 'co' and not 'com).
Updates

Target Market(s)

Women 35-65 years, well-educated, spiritually minded. May have interests like yoga and meditation.

Industry/Entity Type

Health And Wellness

Font styles to use
Sans Serif
Other font styles liked:
• Blue Plaque, Josefina are both great

Colors
fbf289
fdf9cf
cfeae6
33b8a4

Requirements
Must have
• The Palomere logo; my picture.
• Elegance. Calm and expansive feel.
• The poster provided in the project files shows you the kind of information I need to include.
• Colours -- greens and yellows, but the options on pixel harbor are not quite the right shades.
• The logo colour can be changed.
Nice to have
• Classy (but not cliche) image associated with Buddhism; gentle curves similar to those on the business card (see project files).
Should not have
• Dark background. Busy, loud design. Overly 'swirly' design. Images that I have to buy separately.

```html
<!DOCTYPE html>
<html lang="en">
<head>
<meta charset="utf-8">
<title>Palomere Communication Core Course Flyer</title>
<link href="https://fonts.googleapis.com/css2?family=Cinzel:wght@700;900&family=PT+Sans+Narrow:wght@400;700&family=Didact+Gothic&family=Oswald:wght@500;600&family=Open+Sans:wght@400;600&display=swap" rel="stylesheet">
<style>
  :root {
    --page-bg: #e9e7e1;
    --green: #3fae2a;
    --green-light: #8cc63f;
    --green-pale: #cfe8a8;
    --yellow: #fdd73a;
    --blue: #1b48a6;
    --ink: #2b2b2b;
    --ink-soft: #3a3a3a;
    --white: #ffffff;
  }
  * { box-sizing: border-box; margin: 0; padding: 0; }
  html, body { width: 1152px; height: 1200px; overflow: hidden; }
  body { background: var(--page-bg); position: relative; }

  .flyer {
    position: absolute; left: 176px; top: 34px;
    width: 800px; height: 1131px;
    background: var(--white); overflow: hidden;
    box-shadow: 0 4px 18px rgba(0,0,0,.15);
  }
  .hero-photo {
    position: absolute; left: 0; top: 0; width: 800px; height: 480px;
    background:
      radial-gradient(ellipse at 78% 62%, #fff8dc 0%, #f6d68a 30%, rgba(246,214,138,0) 60%),
      linear-gradient(180deg, #f4e2b8 0%, #e9c374 45%, #b98545 70%, #8a5a2c 100%);
  }
  .pebble-photo {
    position: absolute; left: 0; top: 430px; width: 800px; height: 560px;
    background: linear-gradient(180deg, #f1f1ef 0%, #e4e4e1 55%, #f3f3f1 100%);
  }
  .wave { position: absolute; left: 0; top: 330px; width: 800px; height: 150px; }

  .brand {
    position: absolute; top: 40px; right: 36px;
    display: flex; align-items: center; gap: 12px;
    font-family: "Open Sans", sans-serif; font-weight: 600;
    font-size: 30px; color: var(--green);
  }
  .brand-dot { width: 48px; height: 48px; border-radius: 50%; background: var(--green); }

  .headline {
    position: absolute; right: 36px; top: 146px; text-align: right;
    font-family: "Cinzel", serif; color: #1d1d1d; font-weight: 700;
  }
  .headline .equation { font-size: 21px; line-height: 1.2; }
  .headline .equation.small { font-size: 17px; }
  .headline .course-name { font-size: 24px; margin-top: 12px; line-height: 1.1; }
  .headline .course-type { font-size: 44px; font-weight: 900; line-height: 1; }

  .date-box {
    position: absolute; left: 39px; top: 409px; width: 305px; height: 222px;
    background: var(--yellow);
    border-bottom-right-radius: 60px 24px;
    box-shadow: 4px 6px 0 var(--green-light);
    padding: 16px 0 0 26px;
    color: #141414;
  }
  .date-box .dates { font-family: "Cinzel", serif; font-weight: 900; font-size: 44px; line-height: 1.1; }
  .date-box .venue { font-family: "Oswald", sans-serif; font-weight: 600; font-size: 28px; line-height: 1.15; margin-top: 6px; }
  .date-box .city,
  .date-box .price { font-family: "Cinzel", serif; font-weight: 700; font-size: 32px; line-height: 1.15; }

  .body-text {
    font-family: "Didact Gothic", sans-serif; color: var(--ink-soft);
    font-size: 17px; line-height: 1.3; text-align: justify;
    position: absolute;
  }
  .intro { left: 410px; top: 502px; width: 354px; }
  .audience { left: 452px; top: 671px; width: 312px; }

  .explore { position: absolute; left: 42px; top: 668px; width: 340px; }
  .explore h2 {
    font-family: "PT Sans Narrow", sans-serif; font-weight: 700;
    font-size: 21px; line-height: 1.3; color: #1d1d1d; margin-bottom: 8px;
  }
  .explore ul { list-style: none; }
  .explore li {
    position: relative; padding-left: 32px;
    font-family: "Didact Gothic", sans-serif; font-size: 18px; line-height: 1.3;
    color: var(--ink); margin-bottom: 5px;
  }
  .explore li svg { position: absolute; left: 0; top: 3px; width: 18px; height: 16px; }

  .booking-tab {
    position: absolute; left: 426px; top: 854px; width: 347px; height: 54px;
    background: var(--blue);
    clip-path: polygon(4% 0, 96% 0, 100% 100%, 0 100%);
    color: var(--white); font-family: "Open Sans", sans-serif; font-weight: 600;
    font-size: 38px; letter-spacing: 1px; text-align: center; line-height: 56px;
  }
  .booking-bar {
    position: absolute; left: 0; top: 906px; width: 800px; height: 42px;
    background: var(--green-light);
    border-top: 3px solid var(--green);
    font-family: "PT Sans Narrow", sans-serif; font-weight: 700;
    color: var(--white); font-size: 24px; line-height: 40px; padding-left: 38px;
  }

  .facilitator-photo {
    position: absolute; left: 39px; top: 967px; width: 148px; height: 108px;
    border: 4px solid var(--green-light);
    background: linear-gradient(135deg, #8a6a3a, #c9a86a);
  }
  .facilitator-bio {
    position: absolute; left: 213px; top: 981px; width: 556px;
    font-family: "Open Sans", sans-serif; font-size: 18px; line-height: 1.4; color: var(--ink);
  }
  .facilitator-bio strong { font-weight: 600; }

  .footer-bar {
    position: absolute; left: 0; top: 1089px; width: 800px; height: 42px;
    background: var(--green);
    font-family: "PT Sans Narrow", sans-serif; font-weight: 700;
    color: var(--white); font-size: 23px; line-height: 42px; padding-left: 42px;
  }
  .footer-web {
    position: absolute; right: 0; top: 1072px; width: 268px; height: 59px;
    background: var(--green-light);
    clip-path: polygon(14% 0, 100% 0, 100% 100%, 0 100%);
    display: flex; align-items: center; justify-content: flex-end; gap: 10px;
    padding: 10px 22px 0 0;
    font-family: "Open Sans", sans-serif; font-size: 23px; color: var(--white);
  }
  .footer-web svg { width: 20px; height: 20px; }
</style>
</head>
<body>
  <main class="flyer">
    <div class="hero-photo" role="img" aria-label="Stone seated Buddha statue with white magnolia blossoms on a woven mat at golden sunset"></div>
    <div class="pebble-photo" role="img" aria-label="Soft-focus bed of pale white pebbles"></div>

    <svg class="wave" viewBox="0 0 800 150" preserveAspectRatio="none" aria-hidden="true">
      <path d="M0 60 C 220 0, 420 10, 800 70 L800 150 L0 150 Z" fill="#ffffff" opacity="0.55"/>
      <path d="M0 58 C 220 0, 430 8, 800 72 L800 100 C 440 40, 230 30, 0 88 Z" fill="#3fae2a"/>
      <path d="M0 88 C 230 30, 440 40, 800 100 L800 120 C 450 70, 240 55, 0 110 Z" fill="#8cc63f"/>
    </svg>

    <div class="brand"><span class="brand-dot"></span><span>Palomere.co</span></div>

    <header class="headline">
      <p class="equation">Mindfulness + Kindness +</p>
      <p class="equation small">Compassionate Communication =</p>
      <h1 class="course-name">Palomere Communication</h1>
      <p class="course-type">Core Course</p>
    </header>

    <section class="date-box">
      <p class="dates">11-12 Dec</p>
      <p class="venue">THORNFIELD CENTRE</p>
      <p class="city">Edinburgh</p>
      <p class="price">(£125/100)</p>
    </section>

    <p class="body-text intro">Palomere Communication can help you increase awareness &amp; compassion in everyday speech (with yourself &amp; others), better understand your own patterns, and build resilience to challenging situations. Choose from:</p>

    <section class="explore">
      <h2>In this 2-day Core Course, we’ll explore:</h2>
      <ul>
        <li><svg viewBox="0 0 18 16"><path d="M1 8 L7 14 L17 2" fill="none" stroke="#3fae2a" stroke-width="3"/></svg>Compassionate Communication;</li>
        <li><svg viewBox="0 0 18 16"><path d="M1 8 L7 14 L17 2" fill="none" stroke="#3fae2a" stroke-width="3"/></svg>Buddhist Teachings On Right Speech, Loving-kindness,<br>Right Effort, And More;</li>
        <li><svg viewBox="0 0 18 16"><path d="M1 8 L7 14 L17 2" fill="none" stroke="#3fae2a" stroke-width="3"/></svg>Mindfulness Practices;</li>
        <li><svg viewBox="0 0 18 16"><path d="M1 8 L7 14 L17 2" fill="none" stroke="#3fae2a" stroke-width="3"/></svg>Choices Available To Us In Our<br>Everyday Speech.</li>
      </ul>
    </section>

    <p class="body-text audience">This workshop will be of interest if you’d like to improve personal and/or professional relationships. Open to all, best suited to those with at least 1 year’s experience with Mindfulness, Buddhism, or Compassionate Communication / NVC.</p>

    <div class="booking-tab">BOOKING:</div>
    <div class="booking-bar">BOOK ONLINE AT TICKETGLADE OR WRITE MIRABEL@PALOMERE.CO</div>

    <div class="facilitator-photo" role="img" aria-label="Portrait photo of the facilitator"></div>
    <p class="facilitator-bio"><strong>Facilitator:</strong> Mirabel Oakhurst is an experienced group facilitator, having worked with a range of organisations and presented at a number of festivals &amp; conferences.</p>

    <div class="footer-bar">Mirabel offers coaching in Palomere Communication.</div>
    <div class="footer-web">
      <svg viewBox="0 0 20 20" aria-hidden="true"><g fill="none" stroke="#fff" stroke-width="1.6"><circle cx="10" cy="10" r="8.5"/><ellipse cx="10" cy="10" rx="3.8" ry="8.5"/><path d="M1.5 10h17M3 5.5h14M3 14.5h14"/></g></svg>
      <span>www.palomere.co</span>
    </div>
  </main>
</body>
</html>
```